New website design

Hello again, we need you to create a basic, standard website with a homepage, 'contact us' page with reply form, 'pricing page' and 'about us' page. We would like to see most design elements carried over from www.tallowpine.com, our primary website. You can also use the front page of the attached brochure as inspiration for the homepage. The second attachment shows the pricing page (image on the right) with vertical columns - that's a good template for you to use on the pricing page for the website. The third attachment contains the text for the pricing page...just don't use that layout, try and duplicate the vertical layout example.
Target Market(s)
hospitals/medical care facilities
Coding
Coded - Design and coding required
Number of Pages Required
4 page
Look and feel

```html
<!DOCTYPE html>
<html lang="en">
<head>
<meta charset="utf-8">
<title>TallowPine Medical — Quality Assembly and Packaging</title>
<link rel="stylesheet" href="https://fonts.googleapis.com/css2?family=Poppins:wght@300;400;500;600&family=Kanit:wght@600;700&family=Khand:wght@600&display=swap">
<style>
:root{
  --blue:#0d5e9c;
  --blue-dark:#0a4d82;
  --blue-soft:#e8f1f8;
  --ink:#1b1f24;
  --muted:#6b7580;
  --navy:#07131f;
  --white:#ffffff;
  --line:#e6ebf0;
}
*{box-sizing:border-box;margin:0;padding:0}
html,body{width:1200px;height:4345px;overflow:hidden}
body{position:relative;background:var(--white);font-family:"Poppins",sans-serif;color:var(--ink)}
.abs{position:absolute}
.photo{position:absolute}
.brand{display:flex;align-items:center;gap:10px;font-family:"Poppins",sans-serif;font-weight:500;color:var(--blue);white-space:nowrap}
.brand-dot{width:34px;height:34px;border-radius:50%;background:var(--blue);flex:none}
.heading{position:absolute;display:flex;align-items:center;gap:10px;font-family:"Kanit",sans-serif;font-weight:700;font-size:34px;letter-spacing:.5px;color:var(--ink);text-transform:uppercase;white-space:nowrap}
.heading .mark{width:44px;height:44px;border-radius:50%;background:var(--blue);flex:none}
.heading.light{color:var(--white)}
.heading.light .mark{background:var(--white)}
.btn{position:absolute;display:flex;align-items:center;gap:16px;height:40px;padding:0 24px 0 4px;border-radius:20px;background:var(--blue);color:var(--white);font-size:13px;font-weight:500;letter-spacing:.5px;text-transform:uppercase;white-space:nowrap}
.btn .ico{width:32px;height:32px;border-radius:50%;background:var(--white);flex:none}
.btn.white{background:var(--white);color:var(--ink)}
.btn.white .ico{background:var(--blue)}
.btn.inflow{position:relative;display:inline-flex}
.nav{position:absolute;top:28px;left:552px;display:flex;gap:34px;font-size:11px;text-transform:uppercase;color:var(--ink)}
.nav .on{color:var(--blue)}
.hero-title{position:absolute;right:62px;top:252px;text-align:right;font-family:"Khand",sans-serif;font-weight:600;font-size:56px;line-height:60px;color:var(--ink)}
.hero-text{position:absolute;right:62px;top:404px;width:420px;text-align:right;font-size:12px;line-height:20px;color:var(--ink)}
.about-block{position:absolute;left:698px;top:889px;width:400px}
.about-block p{font-size:11.2px;line-height:19.5px;color:#4b535c;margin-bottom:8px}
.about-block .btn{margin-top:14px;height:38px}
.center{position:absolute;left:0;width:1200px;text-align:center}
.card{position:absolute;width:272px;background:var(--white);border-radius:18px;box-shadow:0 6px 28px rgba(20,60,100,.1);text-align:center}
.card .tag{position:absolute;left:38px;top:-8px;width:196px;height:76px;border-radius:8px;background:var(--blue);color:var(--white)}
.card .tag small{display:block;margin-top:10px;font-size:11px;text-transform:uppercase}
.card .tag b{display:block;margin-top:4px;font-size:22px;font-weight:500}
.card .lead{margin:108px 20px 0;font-size:12px;line-height:19px;color:var(--ink)}
.card .desc{margin:14px 32px 0;font-size:11.5px;line-height:19.5px;color:var(--muted)}
.card .price{margin-top:16px;font-family:"Khand",sans-serif;font-size:22px;color:var(--blue)}
.card .unit{font-size:9px;color:var(--muted);letter-spacing:1px}
.card.featured{background:var(--blue)}
.card.featured .tag{background:#0b0d10}
.card.featured .lead,.card.featured .desc,.card.featured .price,.card.featured .unit{color:var(--white)}
.team-block{position:absolute;left:61px;top:2146px;width:360px;color:var(--white)}
.team-block .name{font-size:15px;font-weight:500;text-transform:uppercase;line-height:20px}
.team-block .role{font-size:10px;text-transform:uppercase;margin-top:4px;line-height:14px}
.team-block .bio{font-size:11.2px;line-height:19.5px;margin-top:12px}
.team-block .btn{margin-top:12px;height:38px}
.service-circle{position:absolute;width:190px;height:190px;border-radius:50%;overflow:hidden}
.service-circle .label{position:absolute;left:0;bottom:0;width:190px;height:80px;background:var(--blue);border-radius:0 0 95px 95px;color:var(--white);font-size:17px;font-weight:500;line-height:20px;display:flex;align-items:center;justify-content:center;text-align:center;padding-bottom:10px}
.steril-block{position:absolute;left:631px;top:3128px;width:470px;color:var(--white)}
.steril-block p{font-size:12px;line-height:20px;margin-bottom:12px}
.feature{position:absolute;width:200px;text-align:center}
.feature .ring{width:116px;height:116px;margin:0 auto;border-radius:50%;background:var(--white);box-shadow:0 4px 20px rgba(13,94,156,.22);display:flex;align-items:center;justify-content:center}
.feature p{margin-top:14px;font-size:17px;font-weight:500}
.foot-col{position:absolute;top:4062px;color:#c9d3dc;font-size:12px;line-height:27px}
.foot-col h4{font-size:17px;font-weight:500;color:var(--blue);margin-bottom:4px;line-height:24px}
.foot-col .row{display:flex;align-items:flex-start;gap:14px;margin-top:6px;line-height:19px}
.copy{position:absolute;left:0;top:4311px;width:1200px;height:34px;background:var(--blue-dark);color:var(--white);font-size:11px;text-align:center;line-height:34px}
</style>
</head>
<body>

<!-- HERO -->
<div class="photo" role="img" aria-label="Photo of a gloved technician loading a tray into a sterilization chamber" style="left:0;top:0;width:1200px;height:740px;background:linear-gradient(120deg,#c9d6e0 0%,#e7edf2 40%,#d5dde4 70%,#bcc7cf 100%)"></div>
<svg class="abs" style="left:0;top:440px" width="1200" height="300" viewBox="0 0 1200 300">
  <path d="M0 40 C250 210 560 320 820 280 C1000 250 1140 170 1200 145 L1200 300 L0 300 Z" fill="#fff"/>
  <path d="M0 40 C250 210 560 320 820 280 C1000 250 1140 170 1200 145" fill="none" stroke="#0d5e9c" stroke-width="4"/>
</svg>
<div class="brand abs" style="left:58px;top:12px;font-size:32px">
  <span class="brand-dot"></span><span>TallowPine Medical</span>
</div>
<nav class="nav">
  <span class="on">Home</span><span>Services</span><span>About Us</span><span>Pricing</span><span>Support</span>
</nav>
<div class="btn" style="left:960px;top:16px;font-size:15px;letter-spacing:1px;padding-right:18px">
  <span class="ico"></span>(555) 410-2286
</div>
<h1 class="hero-title">Quality Assembly and<br>Packaging</h1>
<p class="hero-text">TallowPine Medical is certified to requirements of ISO 13485:2016 for contract packaging and sterilization of medical products.</p>
<div class="btn" style="left:958px;top:466px;padding-right:26px"><span class="ico"></span>Contact Us</div>

<!-- ABOUT -->
<div class="photo" role="img" aria-label="Sterilization chamber photo" style="left:218px;top:789px;width:136px;height:136px;border-radius:22px;background:linear-gradient(160deg,#e8eef3,#9fb3c4)"></div>
<div class="photo" role="img" aria-label="Medical tubing in a sealed pouch" style="left:106px;top:888px;width:152px;height:154px;border-radius:22px;background:linear-gradient(150deg,#a9cbe8,#5d9bd1)"></div>
<div class="photo" role="img" aria-label="Gloved hand holding a sample tray by equipment" style="left:267px;top:928px;width:196px;height:204px;border-radius:22px;background:linear-gradient(160deg,#eef1f4,#b8c2d6)"></div>
<div class="photo" role="img" aria-label="Robotic assembly line" style="left:178px;top:1054px;width:130px;height:128px;border-radius:22px;background:linear-gradient(160deg,#6f7d8c,#3a4654)"></div>

<h2 class="heading" style="left:684px;top:816px"><span class="mark"></span>About Us</h2>
<div class="about-block">
  <p>TallowPine Medical Inc. offers efficient and FDA compliant assembly, packaging and in-house Hydrogen Peroxide Gas Plasma (HPGP) specific, as well as contract irradiation (gamma and e-beam) sterilization services for the medical device industry. Validation services for manufacturing processes, packaging.</p>
  <p>sterilization are customized to product specific requirements. The company is dedicated to industrial sterilization requirements and meeting the highest of industry standards: FDA registered; ISO 13485:2016 Certified; Audited in accordance with ISO 14937:2009 and compliant with ISO 14644-1 CLASS 7 (Class 10,000) Cleanrooms.</p>
  <div class="btn inflow"><span class="ico" style="width:30px;height:30px"></span>Meet Our Team</div>
</div>

<!-- PRICING -->
<svg class="abs" style="left:0;top:1390px" width="1200" height="480" viewBox="0 0 1200 480">
  <path d="M0 30 C150 60 250 200 420 190 C600 180 640 40 860 60 C1020 75 1080 150 1200 110 L1200 480 L0 480 Z" fill="#f1f4f7"/>
</svg>
<h2 class="heading" style="left:484px;top:1254px"><span class="mark"></span>Our Pricing</h2>
<p class="center" style="top:1332px;font-size:12px;line-height:20px;color:var(--muted)">Allow us to help you navigate every regulatory hurdle that comes with bringing<br>your product to market</p>

<div class="card" style="left:156px;top:1420px;height:404px">
  <div class="tag"><small>Unschedual</small><b>ON SITE</b></div>
  <p class="lead">Emergency Priority service Technicians Typically On- Premeses Witjin 24 Hours</p>
  <p class="desc">Electronic device Failure is one of the few certainties in life. we don't know when mission critical devices will maifiction,but if were prepared and have</p>
  <div class="price">$225</div><div class="unit">HOUR *</div>
  <div class="btn white" style="left:54px;top:342px;height:38px;box-shadow:0 3px 12px rgba(0,0,0,.12)"><span class="ico" style="width:30px;height:30px"></span>Choose Now</div>
</div>
<div class="card featured" style="left:464px;top:1424px;height:428px;border-radius:22px">
  <div class="tag" style="top:-34px"><small>Unschedual</small><b>ON SITE</b></div>
  <p class="lead" style="margin-top:66px">Emergency Priority service Technicians Typically On- Premeses Witjin 24 Hours</p>
  <p class="desc" style="margin:14px 22px 0">Electronic device Failure is one of the few certainties in life. we don't know when mission critical devices will maifiction,but if were prepared and have a plan in place to address unscheduladed device repair-</p>
  <div class="price">$225</div><div class="unit">HOUR *</div>
  <div class="btn white" style="left:54px;top:362px;height:38px"><span class="ico" style="width:30px;height:30px"></span>Choose Now</div>
</div>
<div class="card" style="left:771px;top:1420px;height:404px">
  <div class="tag"><small>Unschedual</small><b>ON SITE</b></div>
  <p class="lead">Emergency Priority service Technicians Typically On- Premeses Witjin 24 Hours</p>
  <p class="desc">Electronic device Failure is one of the few certainties in life. we don't know when mission critical devices will maifiction,but if were prepared and have</p>
  <div class="price">$225</div><div class="unit">HOUR *</div>
  <div class="btn white" style="left:54px;top:342px;height:38px;box-shadow:0 3px 12px rgba(0,0,0,.12)"><span class="ico" style="width:30px;height:30px"></span>Choose Now</div>
</div>

<!-- TEAM -->
<svg class="abs" style="left:0;top:1900px" width="1200" height="600" viewBox="0 0 1200 600">
  <path d="M0 80 C300 20 700 -10 1200 40 L1200 520 C900 600 500 520 0 530 Z" fill="#0d5e9c"/>
  <path d="M780 540 C900 480 1050 440 1200 430 L1200 520 C1000 560 900 560 780 540 Z" fill="#2a78b4" opacity=".5"/>
</svg>
<h2 class="heading light" style="left:60px;top:2060px"><span class="mark"></span>Meet Our Team</h2>
<div class="team-block">
  <div class="name">Marcus Bellweather</div>
  <div class="role">President and CEO</div>
  <p class="bio">For nearly fifteen years, Marcus Bellweather has successfully served as president for TallowPine Medical, Inc. During his tenure, TallowPine Medical has experienced significant growth in industry specific packaging and specialty sterilization services for the medical device industry.</p>
  <div class="btn white inflow"><span class="ico" style="width:30px;height:30px"></span>View More</div>
</div>

<div class="photo" role="img" aria-label="Portrait of the company president" style="left:546px;top:2030px;width:408px;height:314px;border-radius:14px;background:linear-gradient(160deg,#8b8f94,#4d5258)"></div>
<svg class="abs" style="left:730px;top:2013px" width="40" height="40" viewBox="0 0 40 40"><circle cx="20" cy="20" r="18" fill="#fff"/><path d="M13 23 L20 16 L27 23 Z" fill="#1b1f24"/></svg>
<svg class="abs" style="left:730px;top:2327px" width="40" height="40" viewBox="0 0 40 40"><circle cx="20" cy="20" r="18" fill="#fff"/><path d="M13 17 L20 24 L27 17 Z" fill="#1b1f24"/></svg>
<div class="photo" role="img" aria-label="Team member portrait" style="left:994px;top:2005px;width:112px;height:112px;border-radius:10px;background:linear-gradient(160deg,#c9ced4,#5c646e)"></div>
<div class="photo" role="img" aria-label="Team member portrait" style="left:1099px;top:2146px;width:90px;height:98px;border-radius:10px;background:linear-gradient(160deg,#a7adb4,#3f4650)"></div>
<div class="photo" role="img" aria-label="Team member portrait" style="left:979px;top:2245px;width:84px;height:84px;border-radius:10px;background:linear-gradient(160deg,#f1e7dc,#d3b99c)"></div>

<!-- SERVICES -->
<h2 class="heading" style="left:484px;top:2558px"><span class="mark"></span>Our Services</h2>
<div class="service-circle" style="left:148px;top:2644px" role="img" aria-label="Sterilization chamber photo">
  <div style="position:absolute;inset:0;background:linear-gradient(150deg,#dfe6ec,#8fa2b4)"></div>
  <div class="label">Sterilization</div>
</div>
<div class="service-circle" style="left:388px;top:2644px" role="img" aria-label="Packaged medical instruments photo">
  <div style="position:absolute;inset:0;background:linear-gradient(150deg,#c6e1ea,#4f8fa4)"></div>
  <div class="label">Packaging</div>
</div>
<div class="service-circle" style="left:622px;top:2644px" role="img" aria-label="Handshake in a factory photo">
  <div style="position:absolute;inset:0;background:linear-gradient(150deg,#b8c0c8,#5b6470)"></div>
  <div class="label">Contract<br>Manufacturing</div>
</div>
<div class="service-circle" style="left:861px;top:2644px" role="img" aria-label="Lab staff in protective wear photo">
  <div style="position:absolute;inset:0;background:linear-gradient(150deg,#d6e9f5,#6aa6cf)"></div>
  <div class="label">New Product<br>Introduction</div>
</div>

<!-- STERILIZATION SOLUTIONS -->
<svg class="abs" style="left:0;top:2860px" width="1200" height="600" viewBox="0 0 1200 600">
  <defs><linearGradient id="sterilBg" x1="0" x2="1" y1="0" y2="1"><stop offset="0" stop-color="#0e5f9c"/><stop offset="1" stop-color="#0b4e84"/></linearGradient></defs>
  <path d="M0 100 C200 50 400 90 650 60 C900 30 1050 -20 1200 10 L1200 520 C1000 470 850 560 600 520 C400 490 200 560 0 580 Z" fill="url(#sterilBg)"/>
</svg>
<div class="photo" role="img" aria-label="Technician working inside a sterilizer, shown in a large rounded frame" style="left:124px;top:2980px;width:440px;height:360px;border-radius:180px 60px 180px 180px;background:linear-gradient(140deg,#dfe8ef 0%,#9db5c9 55%,#3d6f98 100%)"></div>
<h2 class="heading light" style="left:630px;top:3052px;font-size:31px"><span class="mark"></span>Sterilization Solutions</h2>
<div class="steril-block">
  <p>TallowPine Medical is committed to finding the most suitable and efficient sterilization method for our customers' products.</p>
  <p>TallowPine Medical is certified to requirements of ISO 13485:2016 for contract packaging and sterilization of medical products.</p>
  <p>ISO 14644-1 Class 7 (Class 10,000) state of the art cleanrooms and laminar flow benches provide the highest standard of sterile environment for your procedures.</p>
</div>

<!-- FEATURES -->
<h2 class="heading" style="left:457px;top:3488px"><span class="mark"></span>Our Services</h2>
<div class="feature" style="left:246px;top:3582px">
  <div class="ring"><svg width="54" height="54" viewBox="0 0 54 54" fill="none" stroke="#0d5e9c" stroke-width="3"><circle cx="24" cy="26" r="18"/><path d="M6 26h36M24 8c-8 9-8 27 0 36M24 8c8 9 8 27 0 36"/><path d="M40 36c-5 0-8 4-8 7 0 4 8 11 8 11s8-7 8-11c0-3-3-7-8-7z" fill="#0d5e9c"/></svg></div>
  <p>Our Location</p>
</div>
<div class="feature" style="left:501px;top:3582px">
  <div class="ring"><svg width="54" height="54" viewBox="0 0 54 54" fill="none" stroke="#0d5e9c" stroke-width="3"><circle cx="27" cy="27" r="20"/><circle cx="27" cy="27" r="8" fill="#0d5e9c"/><path d="M27 7v8M27 39v8M7 27h8M39 27h8M13 13l6 6M35 35l6 6M41 13l-6 6M13 41l6-6"/></svg></div>
  <p>Our Facility</p>
</div>
<div class="feature" style="left:756px;top:3582px">
  <div class="ring"><svg width="54" height="54" viewBox="0 0 54 54" fill="none" stroke="#0d5e9c" stroke-width="3"><path d="M20 12h12M23 12v14L14 44h24L29 26V12"/><circle cx="38" cy="12" r="5" fill="#0d5e9c"/></svg></div>
  <p>Our Expertise</p>
</div>

<!-- FOOTER -->
<svg class="abs" style="left:0;top:3800px" width="1200" height="545" viewBox="0 0 1200 545">
  <path d="M0 140 C200 70 300 20 500 20 C750 20 950 0 1200 30 L1200 545 L0 545 Z" fill="#07131f"/>
</svg>
<div class="btn" style="left:364px;top:3915px;height:38px"><span class="ico" style="width:30px;height:30px"></span>Contact Us</div>
<p class="abs" style="left:600px;top:3895px;width:495px;text-align:right;color:var(--white);font-size:20px;line-height:30px;font-weight:300">Allow us to help you navigate every regulatory hurdle that comes with bringing your product to market</p>

<div class="brand abs" style="left:60px;top:4070px;font-size:20px;color:#c9d3dc">
  <span class="brand-dot" style="width:24px;height:24px"></span><span>TallowPine Medical</span>
</div>
<div class="abs" style="left:60px;top:4128px;width:38px;height:38px;border-radius:50%;background:var(--white)"></div>

<div class="foot-col" style="left:338px;width:220px">
  <h4>Site Map</h4>
  - Home<br>- About Us<br>- Services<br>- Support<br>- Career<br>- Contact Us
</div>
<div class="foot-col" style="left:612px;width:250px">
  <h4>Contact Us</h4>
  <div class="row"><svg width="18" height="20" viewBox="0 0 18 20" style="flex:none"><path d="M9 1C5 1 2 4 2 8c0 5 7 11 7 11s7-6 7-11c0-4-3-7-7-7z" fill="#fff"/><circle cx="9" cy="8" r="2.5" fill="#07131f"/></svg><span>418 Cedar Ridge Ave, Linden Falls,<br>CA 90120</span></div>
  <div class="row"><svg width="18" height="14" viewBox="0 0 18 14" style="flex:none"><rect x="1" y="1" width="16" height="12" rx="1" fill="#fff"/><path d="M1 2l8 6 8-6" stroke="#07131f" stroke-width="1.5" fill="none"/></svg><span>info@tallowpine.com</span></div>
  <div class="row"><svg width="18" height="18" viewBox="0 0 18 18" style="flex:none"><path d="M4 1l3 4-2 2c1 3 3 5 6 6l2-2 4 3-2 3C8 17 1 10 1 3z" fill="#fff"/></svg><span>(555) 410-2286</span></div>
  <div class="row"><svg width="18" height="18" viewBox="0 0 18 18" style="flex:none"><rect x="2" y="2" width="10" height="14" rx="1" fill="#fff"/><path d="M14 6c1.5 1.5 1.5 4.5 0 6" stroke="#fff" stroke-width="1.5" fill="none"/></svg><span>(555) 410-2290</span></div>
</div>
<div class="foot-col" style="left:888px;width:260px">
  <h4>Services</h4>
  - Sterilization<br>- Packaging<br>- Contract Manufacturing<br>- New Product Introduction<br>- Validations
</div>

<div class="copy">© 2021 TallowPine Medical - All Right Reserved.</div>

</body>
</html>
```